2016 Spring tune up

We sell automatic pool covers. We need a postcard design for a mailer to be sent to our customers about a yearly tune up , also offering a discount for a fabric replacement for their automatic pool cover system. The attached information and pictures should be included on the postcard. We would like to see designs that include the colors in our address label

Target Market(s)

Current Automatic Pool Cover Owners

Requirements
Must have
• www.rtvmx.com
• Contact info-service@rtvmx.com
• Attached images and documents
Nice to have
• Color match to our attached logo
Should not have
• Should not have pictures with pools without covers.

```html
<!DOCTYPE html>
<html lang="en">
<head>
<meta charset="utf-8">
<title>Yearly Tune Up Specials – Riverview Automatic Pool Covers</title>
<link href="https://fonts.googleapis.com/css2?family=Arimo:ital,wght@0,400;0,700;1,400&family=Open+Sans:ital,wght@0,700;1,700&family=Source+Sans+3:wght@400;700&display=swap" rel="stylesheet">
<style>
  :root{
    --title-blue:#3d8ed0;
    --deep-blue:#0a5e9c;
    --mid-blue:#0d78bd;
    --bright-cyan:#1eb3e6;
    --body-grey:#4a4a4a;
    --ink:#231f20;
    --white:#ffffff;
  }
  *{box-sizing:border-box;margin:0;padding:0}
  html,body{width:1200px;height:928px;overflow:hidden;background:var(--white)}
  .postcard{position:relative;width:1200px;height:928px;overflow:hidden;background:var(--white);font-family:"Arimo",Arial,sans-serif;color:var(--body-grey)}

  .brand{position:absolute;left:45px;top:39px;width:222px;display:flex;align-items:center;gap:8px}
  .brand-square{width:14px;height:14px;background:var(--title-blue);flex:none}
  .brand-name{font-weight:700;font-size:17px;line-height:1.15;color:var(--title-blue)}
  .brand-address{position:absolute;left:45px;top:106px;width:222px;text-align:center;font-size:10px;font-weight:700;line-height:14px;color:var(--ink)}

  .headline{position:absolute;left:358px;top:42px;width:790px;font-weight:700;font-size:56px;line-height:64px;color:var(--title-blue);white-space:nowrap;text-align:justify;text-align-last:justify}

  .service-bar{position:absolute;left:0;width:440px;height:39px;background:linear-gradient(90deg,var(--deep-blue) 0%,var(--mid-blue) 40%,var(--bright-cyan) 100%)}
  .service-name{position:absolute;left:46px;font-weight:700;font-size:35px;color:var(--white);white-space:nowrap;line-height:39px}
  .price-badge{position:absolute;left:426px;width:132px;height:79px;border-radius:50%;background:radial-gradient(ellipse at 40% 30%,var(--mid-blue),var(--deep-blue) 75%);color:var(--white);text-align:center;font-family:"Open Sans",sans-serif}
  .price-badge .lead{display:block;font-style:italic;font-weight:700;font-size:17px;margin-top:8px;line-height:18px}
  .price-badge .amount{display:block;font-weight:700;font-size:40px;line-height:42px}

  .service-copy{position:absolute;left:46px;width:511px;font-size:20.5px;line-height:25.3px;color:var(--body-grey)}
  .service-copy .line{display:block;white-space:nowrap}
  .service-copy .line.full{text-align:justify;text-align-last:justify}
  .service-note{display:block;font-style:italic;font-size:18px;line-height:24px}
  .service-copy.wide{width:1120px}

  .photo-frame{position:absolute;left:595px;top:160px;width:565px;height:382px}

  .offer-band{position:absolute;left:0;top:0;width:1200px;height:928px}
  .offer-title{position:absolute;left:75px;top:734px;font-weight:700;font-size:33px;color:var(--white);white-space:nowrap}
  .offer-text{position:absolute;left:75px;top:780px;width:1095px;font-family:"Source Sans 3",sans-serif;font-size:17.7px;line-height:23px;color:var(--white)}
  .contact{position:absolute;font-weight:700;font-size:23px;line-height:29px;color:var(--white);white-space:nowrap}
  .contact.left{left:75px;top:838px}
  .contact.right{right:42px;top:833px;text-align:right}
  .call-cta{position:absolute;left:400px;top:853px;font-weight:700;font-size:36px;color:var(--white);white-space:nowrap}
</style>
</head>
<body>
<main class="postcard">

  <div class="brand">
    <span class="brand-square"></span>
    <span class="brand-name">Riverview Automatic Pool Covers</span>
  </div>
  <p class="brand-address">2850 N. Harbor Ave.<br>Fairhaven, MI 49301</p>

  <h1 class="headline">YEARLY TUNE UP SPECIALS</h1>

  <!-- Basic -->
  <div class="service-bar" style="top:152px"></div>
  <h2 class="service-name" style="top:152px">Basic Cover Cleaning</h2>
  <div class="price-badge" style="top:133px"><span class="lead">starting at</span><span class="amount">$290</span></div>
  <p class="service-copy" style="top:196px"><span class="line">Cleaning of the top of the cover only</span><span class="line">(up to 2 hours of labor included)</span><span class="service-note">*Does not include adjustments/lubrication</span></p>

  <!-- Mechanical -->
  <div class="service-bar" style="top:291px"></div>
  <h2 class="service-name" style="top:291px">Mechanical Tune Up</h2>
  <div class="price-badge" style="top:272px"><span class="lead">starting at</span><span class="amount">$330</span></div>
  <p class="service-copy" style="top:351px">
    <span class="line full">Removal of debris and cleaning of recessed housing or</span>
    <span class="line full">bench enclosure, lubrication, inspection of all moving</span>
    <span class="line full">parts, tightening track, and making adjustments for</span>
    <span class="line">proper operation (up to 2 hours of labor included)</span>
    <span class="line full">Replacement of End Casting Pulleys to help prevent</span>
    <span class="line">premature rope breakage</span>
    <span class="service-note">*Does not include cleaning of fabric</span>
  </p>

  <!-- Deluxe -->
  <div class="service-bar" style="top:544px"></div>
  <h2 class="service-name" style="top:544px">Deluxe Tune Up</h2>
  <div class="price-badge" style="top:524px"><span class="lead">starting at</span><span class="amount">$495</span></div>
  <p class="service-copy wide" style="top:607px"><span class="line">All of the services provided in the basic cover cleaning and Mechanical tune up plus:</span><span class="line">Replacement of gliders (on under track units only), guides and shear bolt or pin. (up to 3 hours of labor included)</span></p>

  <!-- Photo -->
  <svg class="photo-frame" viewBox="0 0 565 382" role="img" aria-label="Photo of a covered infinity-edge pool overlooking a blue lake under a clear sky, framed by trees">
    <defs>
      <linearGradient id="frameRim" x1="0" y1="0" x2="1" y2="1">
        <stop offset="0" stop-color="#1a9fe0"/><stop offset=".5" stop-color="#0d78bd"/><stop offset="1" stop-color="#3cc3ee"/>
      </linearGradient>
      <linearGradient id="sceneFill" x1="0" y1="0" x2="0" y2="1">
        <stop offset="0" stop-color="#2e62b0"/><stop offset=".45" stop-color="#6fa8d8"/><stop offset=".55" stop-color="#2a7fc0"/><stop offset="1" stop-color="#1a5f98"/>
      </linearGradient>
    </defs>
    <path d="M40 40 C120 -10 330 50 470 20 C540 5 570 60 560 160 C552 260 540 330 470 360 C400 390 330 340 250 330 C160 320 60 340 20 270 C-10 210 -5 70 40 40 Z" fill="url(#frameRim)"/>
    <path d="M52 54 C130 10 330 66 468 36 C528 24 552 70 545 162 C538 255 524 318 466 344 C400 372 330 326 250 316 C165 306 72 326 36 262 C8 208 12 80 52 54 Z" fill="url(#sceneFill)"/>
  </svg>

  <!-- Offer band -->
  <svg class="offer-band" viewBox="0 0 1200 928" aria-hidden="true">
    <defs>
      <linearGradient id="bandFill" x1="0" y1="0" x2="1" y2="0">
        <stop offset="0" stop-color="#0b5f9f"/><stop offset=".55" stop-color="#22b6e8"/><stop offset="1" stop-color="#0b66a8"/>
      </linearGradient>
      <linearGradient id="rim" x1="0" y1="0" x2="1" y2="0">
        <stop offset="0" stop-color="#4d5358"/><stop offset=".35" stop-color="#ffffff"/><stop offset=".7" stop-color="#8e9398"/><stop offset="1" stop-color="#4d5358"/>
      </linearGradient>
    </defs>
    <path d="M0 722 C70 690 150 676 260 682 C380 690 460 708 560 700 C700 690 790 668 900 668 C1020 668 1110 650 1200 622 L1200 928 L0 928 Z" fill="url(#rim)"/>
    <path d="M0 736 C70 704 150 690 260 696 C380 704 460 720 560 712 C700 702 790 680 900 680 C1020 680 1110 664 1200 638 L1200 928 L0 928 Z" fill="url(#bandFill)"/>
  </svg>

  <h2 class="offer-title">20% OFF FABRIC REPLACEMENT AND SPRING TUNE UP SPECIALS</h2>
  <p class="offer-text">Prepay fabric replacement or spring tune up by April 15, 2016 and receive a 20% discount or by April 30, 2016 and receive a 10% discount. (Vanishing/stone lids extra)</p>
  <p class="contact left">Phone: 800-555-0142<br>Fax: 231-555-0187</p>
  <p class="call-cta">Please call for details</p>
  <p class="contact right">E-mail: service@rtvmx.com<br>www.rtvmx.com</p>

</main>
</body>
</html>
```